We are looking to create a graphic that will be used in Facebook posts each week to show the daily Fernvale Bulletin. Attached is an example of what we are looking for. We need to be able to update the forecast. So we will need hi-res vector files. The graphics need to represent the level of mosquito activity: SLIGHT, AVERAGE, INTENSE, EXTREME

```html
<!DOCTYPE html>
<html lang="en">
<head>
<meta charset="utf-8">
<title>Fernvale Bulletin</title>
<link href="https://fonts.googleapis.com/css2?family=Montserrat:wght@800&family=Roboto+Condensed:wght@500&display=swap" rel="stylesheet">
<style>
:root{
  --slight:#33f000;
  --average:#ffa800;
  --average-alt:#ff7a00;
  --intense:#ff0000;
  --extreme:#5a0000;
  --ink:#111;
  --icon:#7a0e0e;
  --track:#dedede;
  --paper:#fff;
}
*{margin:0;padding:0;box-sizing:border-box}
html,body{width:1200px;height:677px;overflow:hidden;background:#3d7a1a}
.canvas{position:relative;width:1200px;height:677px;overflow:hidden}
.backdrop{position:absolute;inset:0;
  background:
    radial-gradient(ellipse 420px 160px at 640px 80px, rgba(214,160,60,.75), transparent 70%),
    linear-gradient(180deg,#5f9a35 0%,#4c8a22 30%,#3c7416 60%,#2a5a0c 100%);}
.banner{position:absolute;left:51px;top:155px;width:1098px;height:126px;
  padding:5px;border-radius:6px;
  background:linear-gradient(90deg,#33f000 0%,#e8c000 40%,#f00000 65%,#5a0000 100%);}
.banner-inner{width:100%;height:100%;background:var(--paper);border-radius:3px;
  display:flex;align-items:center;justify-content:center}
.title{font-family:'Montserrat',sans-serif;font-weight:800;font-size:88px;line-height:1;
  letter-spacing:1px;white-space:nowrap;
  background:linear-gradient(90deg,#2ee000 0%,#66e010 18%,#d8c418 32%,#e8801a 44%,#ee3a08 54%,#e80000 64%,#b00000 82%,#5e0000 100%);
  -webkit-background-clip:text;background-clip:text;color:transparent;padding-top:6px}
.week{position:absolute;left:51px;top:299px;display:flex;gap:14px}
.day{width:145px;height:227px;border:5px solid var(--c);border-radius:6px;background:var(--paper);
  position:relative;font-family:'Roboto Condensed',sans-serif;font-weight:500;color:var(--ink);text-align:center}
.day-name{position:absolute;top:11px;left:0;right:0;font-size:25px;line-height:1}
.day-date{position:absolute;top:42px;left:0;right:0;font-size:25px;line-height:1}
.level{position:absolute;top:186px;left:0;right:0;font-size:24px;line-height:1}
.gauge{position:absolute;left:13px;top:71px;width:109px;height:109px}
.gauge-track{position:absolute;inset:0;border-radius:50%;border:1.5px solid var(--track)}
.gauge-track.inner{inset:17px}
.gauge-fill{position:absolute;inset:0;border-radius:50%;
  background:conic-gradient(from 225deg,#2ee000 0deg,#b8f000 60deg,#ffe400 100deg,#ff8a00 140deg,#f00000 190deg,#6a0000 262deg,#5a0000 270deg,transparent 270deg);
  -webkit-mask-image:radial-gradient(circle,transparent 37px,#000 37.5px,#000 54px,transparent 54.5px),conic-gradient(from 225deg,#000 calc(var(--lvl)*1deg),transparent 0);
  -webkit-mask-composite:source-in;
  mask-image:radial-gradient(circle,transparent 37px,#000 37.5px,#000 54px,transparent 54.5px),conic-gradient(from 225deg,#000 calc(var(--lvl)*1deg),transparent 0);
  mask-composite:intersect}
.gauge-track.cutout{inset:auto;left:22px;top:88px;width:20px;height:22px;border:none}
.bug{position:absolute;left:29px;top:26px;width:51px;height:56px}
.slight{--c:var(--slight);--lvl:95}
.average{--c:var(--average);--lvl:140}
.average.alt{--c:var(--average-alt)}
.intense{--c:var(--intense);--lvl:222}
.extreme{--c:var(--extreme);--lvl:270}
</style>
</head>
<body>
<svg width="0" height="0" style="position:absolute">
  <defs>
    <symbol id="mosquito" viewBox="0 0 60 66">
      <g fill="none" stroke="var(--icon)" stroke-width="2" stroke-linecap="round" stroke-linejoin="round">
        <path d="M27 12 L20 2 M33 12 L40 2"/>
        <path d="M28 22 L16 14 L12 6 M32 22 L44 14 L48 6"/>
        <path d="M28 28 L14 34 L6 44 M32 28 L46 34 L54 44"/>
        <path d="M28 32 L20 46 L16 62 M32 32 L40 46 L44 62"/>
      </g>
      <g fill="var(--icon)">
        <ellipse cx="30" cy="14" rx="3.5" ry="3.5"/>
        <ellipse cx="30" cy="24" rx="4.5" ry="7"/>
        <ellipse cx="30" cy="42" rx="3.2" ry="13"/>
        <path d="M27 24 C16 22 4 30 2 38 C12 38 22 32 28 28 Z"/>
        <path d="M33 24 C44 22 56 30 58 38 C48 38 38 32 32 28 Z"/>
      </g>
    </symbol>
  </defs>
</svg>
<main class="canvas">
  <div class="backdrop" role="img" aria-label="Close-up photo of a striped mosquito resting on green grass"></div>

  <header class="banner"><div class="banner-inner"><h1 class="title">FERNVALE BULLETIN</h1></div></header>

  <section class="week">
    <article class="day slight">
      <div class="day-name">THU</div><div class="day-date">7/21</div>
      <div class="gauge"><div class="gauge-track"></div><div class="gauge-track inner"></div><div class="gauge-fill"></div><svg class="bug"><use href="#mosquito"/></svg></div>
      <div class="level">SLIGHT</div>
    </article>
    <article class="day average">
      <div class="day-name">FRI</div><div class="day-date">7/22</div>
      <div class="gauge"><div class="gauge-track"></div><div class="gauge-track inner"></div><div class="gauge-fill"></div><svg class="bug"><use href="#mosquito"/></svg></div>
      <div class="level">AVERAGE</div>
    </article>
    <article class="day intense">
      <div class="day-name">SAN</div><div class="day-date">7/24</div>
      <div class="gauge"><div class="gauge-track"></div><div class="gauge-track inner"></div><div class="gauge-fill"></div><svg class="bug"><use href="#mosquito"/></svg></div>
      <div class="level">INTENSE</div>
    </article>
    <article class="day extreme">
      <div class="day-name">SUN</div><div class="day-date">7/25</div>
      <div class="gauge"><div class="gauge-track"></div><div class="gauge-track inner"></div><div class="gauge-fill"></div><svg class="bug"><use href="#mosquito"/></svg></div>
      <div class="level">EXTREME</div>
    </article>
    <article class="day average alt">
      <div class="day-name">MON</div><div class="day-date">7/26</div>
      <div class="gauge"><div class="gauge-track"></div><div class="gauge-track inner"></div><div class="gauge-fill"></div><svg class="bug"><use href="#mosquito"/></svg></div>
      <div class="level">AVERAGE</div>
    </article>
    <article class="day intense">
      <div class="day-name">TUE</div><div class="day-date">7/27</div>
      <div class="gauge"><div class="gauge-track"></div><div class="gauge-track inner"></div><div class="gauge-fill"></div><svg class="bug"><use href="#mosquito"/></svg></div>
      <div class="level">INTENSE</div>
    </article>
    <article class="day slight">
      <div class="day-name">WED</div><div class="day-date">7/28</div>
      <div class="gauge"><div class="gauge-track"></div><div class="gauge-track inner"></div><div class="gauge-fill"></div><svg class="bug"><use href="#mosquito"/></svg></div>
      <div class="level">SLIGHT</div>
    </article>
  </section>
</main>
</body>
</html>
```